Tidal Fern Business Cards

We need something new, fun and exciting for business cards. Our current ones are just plain and we need a design that pops. We want name, position held, phone, email on the front, and a 20% discount on the back. I have also uploaded our old business cards creative to see what we are not wanting, and how boring they were and we want something jazzed up from this, cool design and catches people attention.

```html
<!DOCTYPE html>
<html lang="en">
<head>
<meta charset="UTF-8">
<title>Tidal Fern Business Cards</title>
<link href="https://fonts.googleapis.com/css2?family=Outfit:wght@400;700&display=swap" rel="stylesheet">
<style>
  :root {
    --navy: #173c6c;
    --coral: #f07470;
    --paper: #fafafa;
    --backdrop: #d2d2d2;
    --white: #ffffff;
  }
  html, body {
    margin: 0;
    padding: 0;
    overflow: hidden;
  }
  body {
    width: 1200px;
    height: 1053px;
    background: var(--backdrop);
    position: relative;
    font-family: "Outfit", sans-serif;
  }
  .card {
    position: absolute;
    width: 352px;
    height: 352px;
    overflow: hidden;
  }
  .card--front { left: 215px; top: 144px; background: var(--paper); }
  .card--back-a { left: 642px; top: 144px; }
  .card--back-b { left: 215px; top: 557px; }
  .card--back-c { left: 642px; top: 557px; }

  .brand {
    position: absolute;
    top: 174px;
    left: 0;
    right: 0;
  }
  .brand-row {
    position: absolute;
    top: 34px;
    left: 0;
    right: 0;
    display: flex;
    justify-content: center;
    align-items: center;
    gap: 12px;
  }
  .brand-dot {
    width: 26px;
    height: 26px;
    border-radius: 50%;
    background: var(--coral);
  }
  .brand-name {
    font-weight: 700;
    font-size: 40px;
    color: var(--navy);
    letter-spacing: -0.5px;
    line-height: 1;
  }
  .holder {
    position: absolute;
    top: 138px;
    left: 0;
    right: 0;
    text-align: center;
  }
  .holder-name {
    font-weight: 700;
    font-size: 30px;
    color: var(--coral);
    line-height: 1;
  }
  .holder-role {
    font-weight: 400;
    font-size: 22px;
    color: var(--navy);
    line-height: 1;
    margin-top: 2px;
  }
  .contacts {
    position: absolute;
    left: 35px;
    width: 287px;
    top: 250px;
    color: var(--navy);
    font-size: 15px;
  }
  .contacts-row {
    display: flex;
    border-top: 1px dashed var(--coral);
    height: 37px;
    align-items: center;
  }
  .contacts-row--split .contacts-phone {
    width: 121px;
    padding-left: 1px;
    border-right: 1px dashed var(--coral);
    height: 100%;
    display: flex;
    align-items: center;
  }
  .contacts-row--split .contacts-email {
    flex: 1;
    text-align: right;
  }
  .contacts-row--web {
    justify-content: center;
    height: 34px;
    border-bottom: 1px dashed var(--coral);
  }

  .artwork {
    position: absolute;
    inset: 0;
  }
  .artwork--a { background: linear-gradient(160deg, var(--coral) 0%, var(--navy) 45%, var(--navy) 60%, var(--coral) 100%); }
  .artwork--b { background: linear-gradient(200deg, var(--navy) 0%, var(--coral) 55%, var(--navy) 100%); }
  .artwork--c { background: linear-gradient(225deg, var(--navy) 0%, var(--navy) 45%, var(--coral) 100%); }

  .offer {
    position: absolute;
    color: var(--white);
    font-weight: 700;
    font-size: 33px;
    line-height: 32px;
    text-align: center;
  }
  .offer--a { left: 0; right: 0; top: 84px; }
  .offer--c { left: 150px; width: 186px; top: 112px; }

  .offer-band {
    position: absolute;
    left: 0;
    top: 268px;
    width: 272px;
    height: 60px;
    background: var(--white);
    color: var(--navy);
    font-weight: 700;
    font-size: 33px;
    display: flex;
    align-items: center;
    padding-left: 26px;
    box-sizing: border-box;
  }
</style>
</head>
<body>

  <section class="card card--front">
    <div class="brand-row">
      <span class="brand-dot"></span>
      <span class="brand-name">Tidal Fern</span>
    </div>
    <div class="holder">
      <div class="holder-name">Mara Quell</div>
      <div class="holder-role">Owner</div>
    </div>
    <div class="contacts">
      <div class="contacts-row contacts-row--split">
        <span class="contacts-phone">555 218 4076</span>
        <span class="contacts-email">hello@tidalfern.com</span>
      </div>
      <div class="contacts-row contacts-row--web">www.tidalfern.com</div>
    </div>
  </section>

  <section class="card card--back-a">
    <div class="artwork artwork--a" role="img" aria-label="Large coral heart-and-leaf brand illustration on navy"></div>
    <div class="offer offer--a">20%<br>Discount</div>
  </section>

  <section class="card card--back-b">
    <div class="artwork artwork--b" role="img" aria-label="Tilted coral heart-and-leaf brand illustration on navy"></div>
    <div class="offer-band">20% Discount</div>
  </section>

  <section class="card card--back-c">
    <div class="artwork artwork--c" role="img" aria-label="Close-up coral leaf and heart illustration on navy"></div>
    <div class="offer offer--c">20%<br>Discount</div>
  </section>

</body>
</html>
```